Urgent Care Postcard Launch

We are launching a pediatric only urgent care. The postcard will be hand-delivered to local medical providers and business owners.
Updates

Reason: I was traveling with spotty internet and was unable to provide feedback. Thanks for your understanding!

All designs need to have a focus on Urgent Care. Where the lines say "opening soon" it needs to be specific to Urgent Care as a we are already open for primary care. Thanks.

Target Market(s)

Parents/grandparents of children 0-17 years old.

Industry/Entity Type

Medical

Requirements
Must have
• Opening date of September 1, 2014
Hours of operation - weekdays 5pm-9pm/weekends and holidays 9am-5pm
Phone #(405)555-0193
website - www.larchfieldmd.com
Logo
List of things we can treat (see previous flyers)

```html
<!DOCTYPE html>
<html lang="en">
<head>
<meta charset="utf-8">
<title>Larchfield Pediatrics – Urgent Care Postcards</title>
<link href="https://fonts.googleapis.com/css2?family=PT+Sans:wght@400;700&display=swap" rel="stylesheet">
<style>
  :root {
    --backdrop: #141414;
    --card: #ffffff;
    --red: #e1141c;
    --brown: #8a6b45;
    --navy: #1c2a6b;
    --blue: #1f55a8;
    --link: #3a55b0;
    --ink: #222222;
    --grey: #555555;
  }
  * { box-sizing: border-box; margin: 0; padding: 0; }
  html, body { width: 1200px; height: 1143px; overflow: hidden; background: var(--backdrop); }
  body { font-family: "PT Sans", sans-serif; color: var(--ink); }
  .stage { position: absolute; left: 0; top: 0; width: 1260px; height: 1200px; transform: scale(0.9524); transform-origin: 0 0; }
  .card { position: absolute; width: 731px; height: 566px; background: linear-gradient(160deg, #ffffff 0%, #f2f5fa 55%, #e9eef6 100%); overflow: hidden; }
  .card--services { left: 56px; top: 46px; }
  .card--launch { left: 482px; top: 583px; box-shadow: -12px 14px 26px rgba(0,0,0,.55); }
  .abs { position: absolute; }

  .brand { display: flex; align-items: center; gap: 10px; font-weight: 700; color: var(--brown); z-index: 2; }
  .brand__dot { width: 22px; height: 22px; border-radius: 50%; background: var(--red); flex: none; }
  .brand--small { left: 46px; top: 58px; width: 220px; font-size: 27px; line-height: 28px; }
  .brand--large { left: 270px; top: 178px; font-size: 36px; }
  .brand--large .brand__dot { width: 26px; height: 26px; }

  .photo-team { left: 282px; top: 25px; width: 449px; height: 139px; background: linear-gradient(90deg, #c7cfdc, #b7a09a 40%, #c0566f 65%, #d9d3d3); }
  .services__title { left: 53px; top: 172px; font-size: 27px; font-weight: 700; color: var(--brown); }
  .services__list { list-style: none; top: 216px; font-size: 17.5px; line-height: 22px; }
  .services__list li { position: relative; padding-left: 21px; }
  .services__list li::before { content: ""; position: absolute; left: 0; top: 6px; width: 11px; height: 11px; border-radius: 50%; background: var(--red); }
  .services__list--a { left: 56px; }
  .services__list--b { left: 333px; }
  .services__note { left: 56px; top: 473px; width: 258px; font-size: 17px; line-height: 22px; color: var(--red); }
  .services__call { left: 333px; top: 472px; font-size: 22px; font-weight: 700; color: var(--red); }

  .launch__date { left: 0; width: 650px; top: 28px; text-align: center; font-size: 31px; font-weight: 700; color: var(--red); }
  .photo-exam { left: 28px; top: 77px; width: 250px; height: 285px; background: radial-gradient(ellipse at 50% 50%, #f1e6e2 0%, #e9edf4 70%, rgba(233,238,246,0) 100%); }
  .photo-ribbon { left: 555px; top: 0; width: 176px; height: 210px; background: linear-gradient(200deg, #b3131c 0%, #d7c08a 45%, rgba(240,243,248,0) 80%); }
  .launch__urgent { left: 0; width: 731px; top: 343px; text-align: center; font-size: 22px; font-weight: 700; color: var(--red); }
  .launch__line { left: 0; width: 731px; text-align: center; font-size: 22px; }
  .launch__line--walkin { top: 376px; color: var(--navy); }
  .launch__line--care { top: 405px; color: #111; }
  .info__icon { left: 33px; top: 455px; }
  .info__icon--phone { left: 368px; }
  .info__title { font-size: 22px; font-weight: 700; top: 443px; }
  .info__title--hours { left: 87px; color: var(--blue); }
  .info__title--call { left: 426px; color: var(--red); }
  .info__text { top: 471px; font-size: 17px; line-height: 22px; color: var(--grey); }
  .info__text--hours { left: 87px; }
  .info__text--address { left: 426px; }
  .launch__web { left: 0; width: 720px; top: 517px; text-align: center; font-size: 18px; color: var(--link); }
  .badge { left: 640px; top: 475px; width: 73px; height: 73px; }
</style>
</head>
<body>
<div class="stage">

  <section class="card card--services">
    <div class="abs photo-team" role="img" aria-label="Photo of the four pediatric care providers"></div>
    <div class="abs brand brand--small"><span class="brand__dot"></span><span>Larchfield Pediatrics</span></div>
    <h2 class="abs services__title">We can treat</h2>
    <ul class="abs services__list services__list--a">
      <li>Allergies</li>
      <li>Colds and Flu</li>
      <li>Fever</li>
      <li>Flu Shots and Immunizations</li>
      <li>Ear Infections</li>
      <li>Fractures</li>
      <li>Lacerations or Cut Repair</li>
      <li>Stomach Aches</li>
      <li>Sprains and Strains</li>
      <li>Sore Throats</li>
      <li>Vomiting and Diarrhea</li>
    </ul>
    <ul class="abs services__list services__list--b">
      <li>Asthma Attacks (Minor)</li>
      <li>Eye Injury (Minor)</li>
      <li>Migraine</li>
      <li>Injuries</li>
      <li>Wellness Exams</li>
      <li>Pregnancy Testing</li>
      <li>Physicals</li>
      <li>Skin Rashes</li>
      <li>Urinary and Gynecological Infections</li>
      <li>Wart and Skin Tag Removal</li>
    </ul>
    <p class="abs services__note">No appointment is necessary and it is a walk-in clinic.</p>
    <p class="abs services__call">Call Now! 405-555-0193</p>
  </section>

  <section class="card card--launch">
    <div class="abs photo-ribbon" role="img" aria-label="Red ribbon and golden scissors for a ribbon cutting"></div>
    <h1 class="abs launch__date">OPENING DATE OF SEP 1, 2014</h1>
    <div class="abs photo-exam" role="img" aria-label="Photo of a doctor listening to a toddler's chest with a stethoscope"></div>
    <div class="abs brand brand--large"><span class="brand__dot"></span><span>Larchfield Pediatrics</span></div>
    <p class="abs launch__urgent">Urgent Care</p>
    <p class="abs launch__line launch__line--walkin">No appointment is necessary and it is a walk-in clinic</p>
    <p class="abs launch__line launch__line--care">Nothing matter more that your child health</p>

    <svg class="abs info__icon" width="44" height="44" viewBox="0 0 44 44" aria-hidden="true">
      <circle cx="22" cy="23" r="18" fill="none" stroke="#1f55a8" stroke-width="4"/>
      <path d="M22 12 V23 L15 28" fill="none" stroke="#1f55a8" stroke-width="3.5" stroke-linecap="round"/>
      <path d="M10 4 L4 10 M34 4 L40 10" stroke="#1f55a8" stroke-width="4" stroke-linecap="round"/>
    </svg>
    <p class="abs info__title info__title--hours">Hours of operation</p>
    <p class="abs info__text info__text--hours">weekdays 5pm-9pm/weekends<br>and holidays 9am-5pm</p>

    <svg class="abs info__icon info__icon--phone" width="44" height="44" viewBox="0 0 44 44" aria-hidden="true">
      <path d="M9 8 L15 6 L19 15 L14 18 C16 24 20 28 26 30 L29 25 L38 29 L36 35 C34 39 28 40 22 36 C14 31 9 24 7 16 C6 12 7 10 9 8 Z" fill="#e1141c"/>
      <path d="M26 10 A10 10 0 0 1 34 18 M27 4 A16 16 0 0 1 40 17" fill="none" stroke="#e1141c" stroke-width="3" stroke-linecap="round"/>
    </svg>
    <p class="abs info__title info__title--call">Call Now! 405-555-0193</p>
    <p class="abs info__text info__text--address">1450 SW 88th<br>Oklahoma City, OK 73159</p>

    <p class="abs launch__web">www.larchfieldmd.com</p>
    <svg class="abs badge" viewBox="0 0 73 73" aria-hidden="true">
      <path d="M73 0 V73 H0 Z" fill="#2a68b8"/>
      <circle cx="40" cy="42" r="20" fill="#d9dde6" stroke="#ffffff" stroke-width="3"/>
    </svg>
  </section>

</div>
</body>
</html>
```